Building and Maintenance Company requires a flyer design, Specialising in domestic and commercial bu

We need a flyer design for a company based in Melbourne Victoria, we want to send the flyer out to businesses to obtain more work.

KEV Building and Construction provides the solution for all your building and maintenance needs

We have a professional and highly regarded team of reliable and skilled tradesmen who specialise in building services, domestic and commercial maintenance and gardening in Victoria and Tasmania.

Include our contact details;
0412 738 206
info@kevbuilding.example.au
www.kevbuilding.example.au

Target Market(s)

Domestic and Commercial Clients looking for building maintenance, window cleaning or gardening

Industry/Entity Type

It Company

Font styles to use
Sans Serif

Colors
33b8a4
474747
ffffff

Requirements
Must have
• Images and colour
Nice to have
• We would like the flyer to have our contact details on it.
• Colourful
• Clearly explains what we do, which is, 'KEV Building and Construction provides the solution for all your building, maintenance and gardening needs.'

```html
<!DOCTYPE html>
<html lang="en">
<head>
<meta charset="utf-8">
<title>KEV Building and Construction – Flyer</title>
<link href="https://fonts.googleapis.com/css2?family=Jost:wght@400;500;600&display=swap" rel="stylesheet">
<style>
  :root {
    --teal: #33b8a4;
    --charcoal: #474747;
    --ink: #2f2f2f;
    --white: #ffffff;
    --grey-light: #c4c4c4;
    --sky-top: #5f95cf;
    --sky-low: #b7d2ee;
  }
  * { box-sizing: border-box; margin: 0; padding: 0; }
  html, body {
    width: 900px; height: 1200px; overflow: hidden;
    background: var(--white);
    font-family: "Jost", "Futura", sans-serif;
  }
  .flyer { position: relative; width: 900px; height: 1200px; overflow: hidden; }
  .flyer__art { position: absolute; inset: 0; }

  .headline {
    position: absolute; right: 73px; top: 552px; text-align: right;
    color: var(--ink);
  }
  .headline__name { font-size: 56px; font-weight: 500; line-height: 1; letter-spacing: 0.5px; }
  .headline__slogan { font-size: 30px; font-weight: 500; line-height: 1.2; margin-right: 40px; margin-top: 4px; }

  .section-label {
    position: absolute; left: 70px;
    background: var(--teal);
    color: var(--ink);
    font-size: 24px; font-weight: 500; line-height: 33px;
    padding: 0 12px 0 8px;
    box-shadow: 2px 3px 4px rgba(0,0,0,0.18);
  }
  .section-label--about { top: 687px; width: 158px; }
  .section-label--services { top: 815px; width: 181px; }
  .section-label--contact { top: 1026px; left: 66px; width: 183px; }

  .copy {
    position: absolute; left: 118px; width: 708px;
    font-size: 17px; line-height: 21px; color: var(--ink);
    text-align: justify;
  }
  .copy--about { top: 736px; }
  .copy--services-1 { top: 864px; }
  .copy--services-2 { top: 944px; }

  .contact-list { position: absolute; left: 108px; top: 1078px; list-style: none; }
  .contact-list__item {
    display: flex; align-items: center; gap: 9px;
    font-size: 21px; color: var(--ink); line-height: 32px;
  }
  .contact-list__icon { width: 24px; height: 24px; flex: none; }

  .brand {
    position: absolute; right: 46px; top: 1062px;
    display: flex; align-items: flex-start; gap: 12px;
  }
  .brand__mark { width: 22px; height: 22px; background: var(--teal); margin-top: 6px; }
  .brand__name {
    font-size: 26px; font-weight: 600; line-height: 1.15;
    color: var(--charcoal); text-transform: uppercase; letter-spacing: 1px;
  }
</style>
</head>
<body>
<main class="flyer">
  <svg class="flyer__art" width="900" height="1200" viewBox="0 0 900 1200">
    <defs>
      <linearGradient id="sky" x1="0" y1="0" x2="0.3" y2="1">
        <stop offset="0" stop-color="#5f95cf"/>
        <stop offset="1" stop-color="#b7d2ee"/>
      </linearGradient>
      <linearGradient id="panel" x1="1" y1="0" x2="0.15" y2="1">
        <stop offset="0" stop-color="#c4c4c4"/>
        <stop offset="0.55" stop-color="#ededed"/>
        <stop offset="1" stop-color="#ffffff"/>
      </linearGradient>
    </defs>
    <polygon class="hero-photo" role="img" aria-label="Photo of a heavy crane hook against a blue sky with a tower crane behind"
             points="0,0 900,0 900,349 0,661" fill="url(#sky)"/>
    <polygon class="accent-band" points="0,661 900,349 900,440" fill="#33b8a4"/>
    <polygon class="content-panel" points="0,661 900,440 900,1200 0,1200" fill="url(#panel)"/>
  </svg>

  <header class="headline">
    <h1 class="headline__name">KEV Building</h1>
    <p class="headline__slogan">solutions that last</p>
  </header>

  <h2 class="section-label section-label--about">About Us:</h2>
  <p class="copy copy--about">KEV Building and Construction provides the solution for all your building, maintenance and gardening needs. Based in Melbourne, we serve domestic and commercial clients across Victoria and Tasmania with care and reliability.</p>

  <h2 class="section-label section-label--services">Our services:</h2>
  <p class="copy copy--services-1">Our professional and highly regarded team of reliable, skilled tradesmen specialises in building services, renovations and repairs, plus planned domestic and commercial maintenance that keeps your property safe and working well.</p>
  <p class="copy copy--services-2">We also provide window cleaning and gardening, from regular lawn and garden care to seasonal tidy-ups, so one trusted team looks after your home or business inside and out. Call us today for a free, no-obligation quote.</p>

  <h2 class="section-label section-label--contact">Contact Us:</h2>
  <ul class="contact-list">
    <li class="contact-list__item">
      <svg class="contact-list__icon" viewBox="0 0 24 24" aria-hidden="true">
        <circle cx="12" cy="12" r="10" fill="none" stroke="#2f2f2f" stroke-width="2"/>
        <path d="M9 7c-1 1-1 3 1 6s4 4 5 3l1-1-2-2-1 1c-1-.5-2-2-2.5-3l1-1-2-2z" fill="#2f2f2f"/>
      </svg>
      <span>0412 738 206</span>
    </li>
    <li class="contact-list__item">
      <svg class="contact-list__icon" viewBox="0 0 24 24" aria-hidden="true">
        <circle cx="12" cy="12" r="10" fill="none" stroke="#2f2f2f" stroke-width="2"/>
        <circle cx="12" cy="12" r="5" fill="none" stroke="#2f2f2f" stroke-width="1.6"/>
        <line x1="7" y1="12" x2="17" y2="12" stroke="#2f2f2f" stroke-width="1.4"/>
        <line x1="12" y1="7" x2="12" y2="17" stroke="#2f2f2f" stroke-width="1.4"/>
      </svg>
      <span>www.kevbuilding.example.au</span>
    </li>
    <li class="contact-list__item">
      <svg class="contact-list__icon" viewBox="0 0 24 24" aria-hidden="true">
        <circle cx="12" cy="12" r="10" fill="none" stroke="#2f2f2f" stroke-width="2"/>
        <rect x="6.5" y="8.5" width="11" height="7.5" fill="none" stroke="#2f2f2f" stroke-width="1.5"/>
        <path d="M6.5 8.5l5.5 4 5.5-4" fill="none" stroke="#2f2f2f" stroke-width="1.5"/>
      </svg>
      <span>info@kevbuilding.example.au</span>
    </li>
  </ul>

  <div class="brand">
    <span class="brand__mark" aria-hidden="true"></span>
    <p class="brand__name">KEV Building<br>and<br>Construction</p>
  </div>
</main>
</body>
</html>
```